Business cards

I would like a black background with the design I previously chose. I need 2 sets of cards. Mine will have Rebecca Halvorsen, Broker/Owner, 307-418-2736 and rebecca.pinecrestrealty@mailvane.com
The second set will read, Dana Wexford, Realtor 307-582-4069, dana.pinecrestrealty@mailvane.com

```html
<!DOCTYPE html>
<html lang="en">
<head>
<meta charset="utf-8">
<title>Business Cards – Rebecca Halvorsen &amp; Dana Wexford</title>
<link href="https://fonts.googleapis.com/css2?family=Montserrat:wght@300;400;700&display=swap" rel="stylesheet">
<style>
  :root {
    --backdrop: #d6d6d6;
    --card-dark: #1c1c1c;
    --card-light: #2b2b2b;
    --card-edge: #0b0b0b;
    --ink-white: #f4f4f4;
    --ink-grey: #9a9a9a;
  }
  * { box-sizing: border-box; margin: 0; padding: 0; }
  html, body {
    width: 1200px;
    height: 800px;
    overflow: hidden;
    background: var(--backdrop);
    font-family: "Montserrat", sans-serif;
  }
  .card-sheet {
    width: 1200px;
    height: 800px;
    display: flex;
    align-items: center;
    justify-content: center;
    gap: 40px;
  }
  .business-card {
    width: 540px;
    height: 309px;
    border: 7px solid var(--card-edge);
    background: radial-gradient(ellipse at 40% 30%, var(--card-light), var(--card-dark) 75%);
    display: flex;
    align-items: center;
    justify-content: center;
    box-shadow: 0 2px 4px rgba(0,0,0,0.25);
  }
  .card-content {
    display: flex;
    align-items: center;
    gap: 12px;
  }
  .identity {
    text-align: right;
  }
  .identity__name {
    color: var(--ink-white);
    font-weight: 700;
    font-size: 16px;
    letter-spacing: 1.6px;
    text-transform: uppercase;
    line-height: 1.15;
  }
  .identity__title {
    color: var(--ink-grey);
    font-weight: 300;
    font-size: 12px;
    letter-spacing: 0.6px;
    margin-top: 2px;
  }
  .divider {
    width: 2px;
    height: 38px;
    background: var(--ink-white);
  }
  .contact {
    list-style: none;
    display: flex;
    flex-direction: column;
    gap: 4px;
  }
  .contact__item {
    display: flex;
    align-items: center;
    gap: 6px;
    color: var(--ink-white);
    font-size: 11px;
    font-weight: 400;
    letter-spacing: 0.3px;
  }
  .contact__icon {
    width: 10px;
    height: 10px;
    fill: var(--ink-white);
    flex: none;
  }
</style>
</head>
<body>
  <main class="card-sheet">
    <article class="business-card">
      <div class="card-content">
        <div class="identity">
          <h1 class="identity__name">Rebecca Halvorsen</h1>
          <p class="identity__title">Broker/Owner</p>
        </div>
        <span class="divider"></span>
        <ul class="contact">
          <li class="contact__item">
            <svg class="contact__icon" viewBox="0 0 10 10" aria-hidden="true"><path d="M2.2 0.5 L3.6 2.6 L2.8 3.6 Q3.6 5.6 6.4 7.2 L7.4 6.4 L9.5 7.8 L8.6 9.4 Q4.8 9.6 2.4 7 Q0.2 4.4 0.6 1.4 Z"/></svg>
            <span>307-418-2736</span>
          </li>
          <li class="contact__item">
            <svg class="contact__icon" viewBox="0 0 10 10" aria-hidden="true"><path d="M0.5 2 H9.5 V8.5 H0.5 Z M1.2 2.6 L5 5.6 L8.8 2.6 Z" fill-rule="evenodd"/></svg>
            <span>rebecca.pinecrestrealty@mailvane.com</span>
          </li>
        </ul>
      </div>
    </article>

    <article class="business-card">
      <div class="card-content">
        <div class="identity">
          <h1 class="identity__name">Dana Wexford</h1>
          <p class="identity__title">Realtor</p>
        </div>
        <span class="divider"></span>
        <ul class="contact">
          <li class="contact__item">
            <svg class="contact__icon" viewBox="0 0 10 10" aria-hidden="true"><path d="M2.2 0.5 L3.6 2.6 L2.8 3.6 Q3.6 5.6 6.4 7.2 L7.4 6.4 L9.5 7.8 L8.6 9.4 Q4.8 9.6 2.4 7 Q0.2 4.4 0.6 1.4 Z"/></svg>
            <span>307-582-4069</span>
          </li>
          <li class="contact__item">
            <svg class="contact__icon" viewBox="0 0 10 10" aria-hidden="true"><path d="M0.5 2 H9.5 V8.5 H0.5 Z M1.2 2.6 L5 5.6 L8.8 2.6 Z" fill-rule="evenodd"/></svg>
            <span>dana.pinecrestrealty@mailvane.com</span>
          </li>
        </ul>
      </div>
    </article>
  </main>
</body>
</html>
```